" A Trilo Sistemas é uma empresa que desenvolve sistemas de monitoramento remoto, telemetria via satélite, telecontrole, automaçao, rastreamento de veículos e etc.. Trata-se de uma empresa moderna e jovem, com uma linguagem de comunicaçao moderna e descontraída, sem perder a seriedade. Temos dois segmentos: Corporativo e Varejo. No corporativo, prestamos serviço para grandes empresas como Pedra Alta Minérios por exemplo.Já no varejo atendemos pessoas fisicas ou pequenas empresas. "

```html
<!DOCTYPE html>
<html lang="pt-BR">
<head>
<meta charset="utf-8">
<title>Trilo Sistemas</title>
<link rel="stylesheet" href="https://fonts.googleapis.com/css2?family=Montserrat:wght@400;600;700;800&display=swap">
<style>
:root{
  --orange:#e2652a;
  --orange-dark:#c44f1c;
  --teal:#3d6f8c;
  --teal-dark:#2c5670;
  --navy:#1f4660;
  --grey:#6b6b6b;
  --light:#f2f2f2;
  --white:#ffffff;
}
*{margin:0;padding:0;box-sizing:border-box}
html,body{width:1200px;height:1200px;overflow:hidden;background:var(--white);font-family:'Montserrat',sans-serif}
.page{position:absolute;left:336px;top:0;width:528px;height:1200px;background:var(--white);overflow:hidden}
.abs{position:absolute}

/* hero */
.hero{left:0;top:0;width:528px;height:250px}
.hero-photo{left:0;top:0;width:528px;height:250px;background:linear-gradient(160deg,#2d5d70 0%,#6a4b3a 35%,#b86a3a 60%,#2f4c5d 100%)}
.brand{left:18px;top:6px;display:flex;align-items:center;gap:6px;color:var(--white);font-weight:700;font-size:16px}
.brand-dot{width:14px;height:14px;border-radius:50%;background:var(--white)}
.nav{left:206px;top:0;display:flex}
.nav a{display:block;padding:7px 8px;font-size:8px;font-weight:700;color:var(--white);background:var(--orange);text-decoration:none}
.nav a.active{background:var(--orange-dark)}
.hero-title{left:120px;top:36px;width:400px;color:var(--white);font-weight:800;font-size:15px;text-align:right}
.hero-sub{left:120px;top:58px;width:400px;color:var(--white);font-size:9px;text-align:right}
.hero-btn{left:432px;top:92px;background:var(--orange);color:var(--white);font-size:7px;font-weight:700;padding:4px 8px;border-radius:2px}
.hero-wave{left:0;top:210px;width:528px;height:50px}

/* about */
.about-mark{left:66px;top:298px;width:50px;height:50px;border-radius:50%;border:4px solid var(--teal)}
.about-title{left:28px;top:360px;width:220px;color:var(--teal);font-weight:800;font-size:20px}
.about-text{left:60px;top:388px;width:200px;color:var(--grey);font-size:10px;line-height:1.35}
.about-text em{font-style:normal;color:var(--teal);text-decoration:underline}
.hexes{left:230px;top:246px;width:290px;height:230px}

/* showcase */
.showcase{left:0;top:480px;width:528px;height:310px}
.showcase-title{left:0;top:530px;width:528px;text-align:center;color:var(--white);font-weight:800;font-size:20px}
.showcase-sub{left:0;top:556px;width:528px;text-align:center;color:var(--white);font-size:10px;line-height:1.35}
.showcase-sub em{font-style:normal;text-decoration:underline}
.devices{left:144px;top:598px;width:240px;height:140px;border-radius:4px;background:linear-gradient(135deg,#e4e6e8 0%,#4a5660 40%,#3a4650 70%,#d8dadc 100%)}
.showcase-btn{left:228px;top:754px;width:72px;height:20px;border:1.5px solid var(--white);color:var(--white);font-size:7px;font-weight:700;text-align:center;line-height:17px;border-radius:2px}

/* contact */
.contact-title{left:0;top:800px;width:528px;text-align:center;color:var(--navy);font-weight:800;font-size:21px}
.map{left:96px;top:832px;width:336px;height:136px;background:linear-gradient(135deg,#cfdcc4 0%,#e8e6de 45%,#a9c7dd 70%,#dfe6d6 100%)}
.map-pin{left:140px;top:842px;width:22px;height:30px}
.field{border:1px solid #cfcfcf;background:var(--white);color:#9a9a9a;font-size:6px;padding:3px 5px}
.field-name{left:130px;top:986px;width:124px;height:14px}
.field-mail{left:274px;top:986px;width:124px;height:14px}
.field-msg{left:130px;top:1010px;width:268px;height:50px}
.send-btn{left:350px;top:1066px;width:48px;height:15px;background:var(--orange);color:var(--white);font-size:7px;font-weight:700;text-align:center;line-height:15px}
.perks{left:64px;top:1098px;width:400px;display:flex;justify-content:space-between}
.perk{width:90px;text-align:center;color:var(--grey);font-size:5px;line-height:1.3}
.perk svg{display:block;margin:0 auto 4px}
.perk strong{font-size:7px;color:var(--navy)}
.footer{left:36px;top:1160px;width:456px;height:40px;background:var(--teal);display:flex;align-items:center;justify-content:center;gap:6px;color:var(--white);font-weight:700;font-size:14px}
.footer .brand-dot{width:11px;height:11px}
</style>
</head>
<body>
<div class="page">

  <header class="abs hero">
    <div class="abs hero-photo" role="img" aria-label="Fotomontagem de tecnologia: mão segurando globo, notebook, avião e caminhão"></div>
    <div class="abs brand"><span class="brand-dot"></span>trilo</div>
    <nav class="abs nav">
      <a class="active">HOME</a><a>Tecnologia</a><a>Segmentos</a><a>Serviços</a><a>Trilo Web</a>
    </nav>
    <h1 class="abs hero-title">só a trilo tem a tecnologia que move o mundo</h1>
    <p class="abs hero-sub">somos apaixonados por Monitoramento &amp; Segurança</p>
    <div class="abs hero-btn">saiba mais →</div>
    <svg class="abs hero-wave" viewBox="0 0 528 50" preserveAspectRatio="none">
      <path d="M0 20 Q264 60 528 14 L528 50 L0 50 Z" fill="var(--orange)"/>
      <path d="M0 28 Q264 66 528 22 L528 50 L0 50 Z" fill="var(--white)"/>
    </svg>
  </header>

  <section>
    <div class="abs about-mark"></div>
    <h2 class="abs about-title">A TRILO MUDOU !</h2>
    <p class="abs about-text">Estamos sempre trabalhando<br>para <em>melhorar pra você</em> !</p>
    <svg class="abs hexes" viewBox="0 0 290 230">
      <defs>
        <linearGradient id="gConsult" x1="0" y1="0" x2="1" y2="1"><stop offset="0" stop-color="#c9b8a6"/><stop offset="1" stop-color="#7a6a5c"/></linearGradient>
        <linearGradient id="gTec" x1="0" y1="0" x2="1" y2="1"><stop offset="0" stop-color="#8fc0e0"/><stop offset="1" stop-color="#3f7ea8"/></linearGradient>
        <linearGradient id="gSol" x1="0" y1="0" x2="1" y2="1"><stop offset="0" stop-color="#b9a27a"/><stop offset="1" stop-color="#6d8a4a"/></linearGradient>
      </defs>
      <g>
        <polygon points="50,10 92,34 92,82 50,106 8,82 8,34" fill="#1d2a33" stroke="var(--orange)" stroke-width="4"/>
        <text x="50" y="50" text-anchor="middle" fill="#fff" font-size="9" font-weight="700">A EMPRESA</text>
        <rect x="30" y="60" width="40" height="11" fill="none" stroke="#fff" stroke-width="1"/>
        <text x="50" y="68" text-anchor="middle" fill="#fff" font-size="5">saiba mais</text>
      </g>
      <g role="img" aria-label="Foto de consultoria em reunião">
        <polygon points="140,2 182,26 182,74 140,98 98,74 98,26" fill="url(#gConsult)" stroke="var(--orange)" stroke-width="4"/>
        <rect x="104" y="44" width="72" height="12" fill="#fff"/>
        <text x="140" y="53" text-anchor="middle" fill="var(--navy)" font-size="7" font-weight="700">CONSULTORIA</text>
      </g>
      <g role="img" aria-label="Foto de avião representando tecnologia">
        <polygon points="68,110 110,134 110,182 68,206 26,182 26,134" fill="url(#gTec)" stroke="var(--orange)" stroke-width="4"/>
        <text x="68" y="176" text-anchor="middle" fill="#fff" font-size="7" font-weight="700">TECNOLOGIA</text>
      </g>
      <g role="img" aria-label="Foto de paisagem industrial representando soluções">
        <polygon points="160,100 202,124 202,172 160,196 118,172 118,124" fill="url(#gSol)" stroke="var(--orange)" stroke-width="4"/>
        <text x="160" y="166" text-anchor="middle" fill="#fff" font-size="7" font-weight="700">SOLUÇÕES</text>
      </g>
    </svg>
  </section>

  <section>
    <svg class="abs showcase" viewBox="0 0 528 310" preserveAspectRatio="none">
      <path d="M0 30 Q264 -10 528 30 L528 310 L0 310 Z" fill="var(--orange)"/>
      <path d="M0 38 Q264 0 528 38 L528 310 L0 310 Z" fill="var(--teal)"/>
    </svg>
    <h2 class="abs showcase-title">LOREM IPSUM DOLOR</h2>
    <p class="abs showcase-sub">Estamos sempre trabalhando<br>para <em>melhorar pra você</em> !</p>
    <div class="abs devices" role="img" aria-label="Ilustração de monitor, tablet e celular exibindo o vídeo e o aplicativo da empresa"></div>
    <div class="abs showcase-btn">SAIBA MAIS</div>
  </section>

  <section>
    <h2 class="abs contact-title">CONTATO</h2>
    <div class="abs map" role="img" aria-label="Mapa com a localização da empresa"></div>
    <svg class="abs map-pin" viewBox="0 0 22 30"><path d="M11 0C5 0 0 5 0 11c0 8 11 19 11 19s11-11 11-19C22 5 17 0 11 0z" fill="var(--teal)"/><circle cx="11" cy="11" r="4" fill="#fff"/></svg>
    <div class="abs field field-name">Digite seu nome</div>
    <div class="abs field field-mail">Digite seu e-mail</div>
    <div class="abs field field-msg">Digite sua mensagem</div>
    <div class="abs send-btn">ENVIAR</div>

    <div class="abs perks">
      <div class="perk">
        <svg width="30" height="30" viewBox="0 0 30 30"><rect x="7" y="4" width="16" height="22" rx="2" fill="none" stroke="var(--orange)" stroke-width="2"/><path d="M11 12h8M11 16h8M11 20h5" stroke="var(--orange)" stroke-width="2"/></svg>
        Atendimento online de segunda a sexta
      </div>
      <div class="perk">
        <svg width="30" height="30" viewBox="0 0 30 30"><path d="M4 6h18v12H12l-5 5v-5H4z" fill="none" stroke="var(--orange)" stroke-width="2"/></svg>
        Fale com nossa equipe comercial
      </div>
      <div class="perk">
        <svg width="30" height="30" viewBox="0 0 30 30"><path d="M6 18v-4a9 9 0 0 1 18 0v4" fill="none" stroke="var(--orange)" stroke-width="2"/><rect x="4" y="16" width="5" height="8" rx="2" fill="var(--orange)"/><rect x="21" y="16" width="5" height="8" rx="2" fill="var(--orange)"/></svg>
        Suporte técnico todos os dias
      </div>
      <div class="perk">
        <svg width="30" height="30" viewBox="0 0 30 30"><path d="M9 5l4 5-3 3a14 14 0 0 0 7 7l3-3 5 4-3 4C12 25 5 18 5 8z" fill="var(--orange)"/></svg>
        <strong>(31) 4002-1180</strong>
      </div>
    </div>
  </section>

  <footer class="abs footer"><span class="brand-dot"></span>trilo</footer>
</div>
</body>
</html>
```